Letterhead

We are looking for a basic letterhead. It should include our logo, website - northpeakkitchenware.com, phone 907.418.3952, toll free 855.392.6180, and fax 907.418.5263, along with our address 4837 Birchwood Lane, Anchorage, AK 99517. I want something that will look good printed in color or black and white.

```html
<!DOCTYPE html>
<html lang="en">
<head>
<meta charset="utf-8">
<title>North Peak Kitchenware — Letterhead</title>
<link href="https://fonts.googleapis.com/css2?family=Signika:wght@400;600&family=Arimo:wght@400&display=swap" rel="stylesheet">
<style>
  :root {
    --brand-red: #c23a4b;
    --brand-navy: #1f4e8c;
    --ink: #1e1e1e;
    --paper: #ffffff;
    --backdrop: #e4e4e4;
    --signature-ink: #5b74b3;
  }
  * { margin: 0; padding: 0; box-sizing: border-box; }
  html, body {
    width: 935px; height: 1200px; overflow: hidden;
    background: var(--backdrop);
  }
  .letterhead {
    position: absolute; left: 61px; top: 26px;
    width: 812px; height: 1148px;
    background: var(--paper);
    box-shadow: 0 2px 10px rgba(0,0,0,0.15);
    font-family: "Signika", "Trebuchet MS", sans-serif;
    color: var(--ink);
  }
  .brand {
    position: absolute; left: 38px; top: 62px;
    display: flex; align-items: center; gap: 12px;
  }
  .brand-mark {
    width: 18px; height: 18px; background: var(--brand-red);
  }
  .brand-name {
    font-family: "Signika", "Trebuchet MS", sans-serif;
    font-weight: 600; font-size: 30px; line-height: 1.05;
    color: var(--brand-navy); text-transform: uppercase; letter-spacing: 0.5px;
  }
  .contact-box {
    position: absolute; left: 543px; top: 39px;
    width: 269px; height: 116px;
    background: var(--brand-red); color: #fff;
    font-family: "Arimo", Arial, sans-serif; font-size: 14.5px; line-height: 21px;
    padding: 6px 0 0 15px;
  }
  .contact-box .address { margin-top: 2px; }
  .salutation {
    position: absolute; left: 103px; top: 320px;
    font-size: 26px; font-weight: 400;
  }
  .body-copy {
    position: absolute; left: 103px; top: 394px; width: 598px;
    font-size: 13.6px; line-height: 22px; text-align: justify;
  }
  .body-copy p + p { margin-top: 21px; }
  .closing {
    position: absolute; right: 111px; top: 804px;
    font-size: 13.6px;
  }
  .signature {
    position: absolute; left: 588px; top: 888px;
    width: 134px; height: 42px;
    background: linear-gradient(90deg, rgba(91,116,179,0.18), rgba(91,116,179,0.32));
    border-radius: 4px;
  }
  .footer-rule {
    position: absolute; top: 1108px; height: 13px; background: var(--brand-red);
  }
  .footer-rule.left { left: 0; width: 280px; }
  .footer-rule.right { left: 532px; width: 280px; }
  .website {
    position: absolute; top: 1105px; left: 280px; width: 252px;
    text-align: center;
    font-family: "Arimo", Arial, sans-serif; font-size: 14.5px;
  }
</style>
</head>
<body>
  <main class="letterhead">
    <header>
      <div class="brand">
        <span class="brand-mark"></span>
        <div class="brand-name">North Peak<br>Kitchenware</div>
      </div>
      <address class="contact-box" style="font-style: normal;">
        <div>Phone 907.418.3952</div>
        <div>Toll free 855.392.6180</div>
        <div>Fax 907.418.5263</div>
        <div class="address">Address 4837 Birchwood Lane,<br>Anchorage, AK 99517</div>
      </address>
    </header>

    <h1 class="salutation">Dear Mr. Hallett,</h1>

    <section class="body-copy">
      <p>Lorem ipsum dolor sit amet, consectetur adipiscing elit. Donec orci purus, luctus vitae dignissim eu, iaculis sed purus. Vivamus faucibus, ipsum nec aliquet viverra, leo mauris condimentum ligula, sit amet sagittis enim ligula quis arcu. Nam egestas tortor id nisi porttitor mattis. In tortor ante, ultricies in suscipit a, tempus non massa. Vivamus et auctor mi. Fusce vel massa nulla. Phasellus nec eros mauris, et scelerisque orci.</p>
      <p>Donec malesuada orci vitae nulla accumsan porta a id massa. Quisque accumsan iaculis magna sit amet fringilla. Maecenas consequat, magna eget tincidunt semper, odio nibh rutrum mi, id feugiat ante nisi eu risus. Vestibulum nunc orci, rhoncus a placerat in, ultricies in mi. Cras mattis varius eros, vel fringilla nisi suscipit eget. Quisque scelerisque sagittis nulla at porttitor.</p>
      <p>Sed id augue vitae urna euismod commodo aliquet a quam. Pellentesque arcu velit, cursus et malesuada ut, consequat et diam. Nullam erat sem, rhoncus id ullamcorper vitae, rhoncus et arcu. In ultricies ultricies nulla, ut rutrum nisi iaculis at. Donec eu magna a metus ornare faucibus. Fusce aliquet faucibus ultricies. Morbi semper, est id tincidunt gravida, sem arcu adipiscing lacus, ac bibendum nulla leo eu purus. Quisque nec diam sed risus consectetur a ccumsan quis quis nibh. Vestibulum id purus lorem.</p>
    </section>

    <p class="closing">Sincerely,</p>
    <div class="signature" role="img" aria-label="Handwritten signature of Evan Marsh in blue ink"></div>

    <footer>
      <div class="footer-rule left"></div>
      <div class="website">www.northpeakkitchenware.com</div>
      <div class="footer-rule right"></div>
    </footer>
  </main>
</body>
</html>
```